A4 Flyer

Brightwell Care Academy is starting a course in regional Victoria. We are currently advertising (See attached file A34984) in local papers but need to create a one page flyer to distribute to Aged Care facilities in the area. The A4 flyer will be inserted into a folder pack with more detailed information on Brightwell Care Academy. Important to use images and logoes attached

Target Market(s)

Flyer to be distributed to Aged Care facility staff and owners

Industry/Entity Type

Advertising

Font styles to use
Sans Serif

Colors
f37123
ec1f27

Requirements
Must have
• BCA Logo
Some image

```html
<!DOCTYPE html>
<html lang="en">
<head>
<meta charset="utf-8">
<title>Brightwell Care Academy – Fast Track Course Flyer</title>
<link rel="stylesheet" href="https://fonts.googleapis.com/css2?family=Source+Sans+3:wght@400;600;700&display=swap">
<style>
  :root {
    --orange: #f37123;
    --red: #ec1f27;
    --ink: #222222;
    --paper: #ffffff;
    --photo-warm: #d9c8b8;
    --photo-cool: #c9ccd2;
    --font: "Source Sans 3", Arial, sans-serif;
  }
  * { margin: 0; padding: 0; box-sizing: border-box; }
  html, body { width: 849px; height: 1200px; overflow: hidden; background: var(--paper); }
  .flyer {
    position: relative;
    width: 849px;
    height: 1200px;
    font-family: var(--font);
    color: var(--ink);
    overflow: hidden;
  }
  .headline {
    position: absolute;
    left: 40px;
    top: 18px;
    color: var(--orange);
    font-weight: 400;
    font-size: 82px;
    line-height: 92px;
    letter-spacing: 0.5px;
  }
  .course-start {
    position: absolute;
    left: 46px;
    top: 240px;
    color: var(--red);
    font-weight: 600;
    font-size: 29px;
    letter-spacing: -0.3px;
  }
  .brand-name {
    position: absolute;
    left: 600px;
    top: 240px;
    width: 230px;
    color: var(--orange);
    font-weight: 400;
    font-size: 33px;
    line-height: 38px;
    text-align: left;
  }
  .photo {
    position: absolute;
    border-radius: 2px;
  }
  .photo--tutor {
    left: 43px; top: 352px; width: 264px; height: 329px;
    background: linear-gradient(135deg, #e8e4df 0%, var(--photo-warm) 55%, #b98f80 100%);
  }
  .photo--student-a {
    left: 43px; top: 802px; width: 168px; height: 265px;
    background: linear-gradient(160deg, #eeeeee 0%, var(--photo-cool) 50%, #3a3a40 100%);
  }
  .photo--student-b {
    left: 225px; top: 865px; width: 179px; height: 227px;
    background: linear-gradient(160deg, #eeeeee 0%, #dcdcdc 55%, #b8a896 100%);
  }
  .funding-note {
    position: absolute;
    left: 327px;
    top: 350px;
    width: 340px;
    color: var(--red);
    font-size: 18.5px;
    line-height: 22px;
  }
  .subject-list {
    position: absolute;
    left: 327px;
    top: 405px;
    list-style: none;
    font-size: 23px;
    line-height: 35px;
    letter-spacing: 0.3px;
  }
  .qualification-band {
    position: absolute;
    left: 0;
    top: 692px;
    width: 806px;
    height: 89px;
    background: var(--red);
    color: var(--paper);
    text-align: right;
    padding-right: 14px;
  }
  .qualification-band .title {
    display: block;
    padding-right: 6px;
    font-weight: 600;
    font-size: 29px;
    line-height: 46px;
  }
  .qualification-band .subtitle {
    display: block;
    font-size: 25px;
    line-height: 40px;
    letter-spacing: 0.2px;
  }
  .funding-offer {
    position: absolute;
    left: 243px;
    top: 797px;
    font-size: 24.5px;
  }
  .fees {
    position: absolute;
    right: 56px;
    top: 843px;
    font-size: 30px;
  }
  .callout-box {
    position: absolute;
    left: 495px;
    top: 896px;
    width: 314px;
    height: 164px;
    border-radius: 36px;
    background: var(--red);
  }
  .phone-icon {
    position: absolute;
    left: 70px;
    top: 1102px;
    width: 52px;
    height: 42px;
  }
  .phone-number {
    position: absolute;
    left: 35px;
    top: 1154px;
    color: var(--red);
    font-size: 28px;
  }
  .web-address {
    position: absolute;
    left: 238px;
    top: 1153px;
    width: 379px;
    height: 38px;
    border-radius: 8px;
    background: var(--orange);
    color: var(--paper);
    font-size: 26px;
    line-height: 38px;
    text-align: center;
    letter-spacing: 0.3px;
  }
</style>
</head>
<body>
<main class="flyer">
  <h1 class="headline">Unique<br>Opportunity!</h1>
  <p class="course-start">Fast Track Course - Start July 2014</p>
  <p class="brand-name">Brightwell Care Academy</p>

  <div class="photo photo--tutor" role="img" aria-label="Tutor demonstrating on an anatomical torso model"></div>

  <p class="funding-note">This training is delivered with VIC and Comm Govt Funding to eligible students</p>
  <ul class="subject-list">
    <li>Pathology</li>
    <li>Aged Care</li>
    <li>First Aid</li>
    <li>CPR</li>
    <li>Anaphylaxis</li>
    <li>Medications for PCA’s</li>
    <li>Home &amp; Community Care</li>
    <li>Health Services</li>
  </ul>

  <div class="qualification-band">
    <span class="title">DOUBLE QUALIFICATION</span>
    <span class="subtitle">CERT III IN AGED CARE WITH HOME AND COMMUNITY CARE</span>
  </div>

  <div class="photo photo--student-a" role="img" aria-label="Smiling student seated at a classroom desk"></div>
  <div class="photo photo--student-b" role="img" aria-label="Student seated at a classroom desk with notes"></div>

  <p class="funding-offer">Government Funding for eligible students!</p>
  <p class="fees">Fees from $117</p>
  <div class="callout-box"></div>

  <svg class="phone-icon" viewBox="0 0 52 42" aria-hidden="true">
    <path fill="var(--orange)" d="M4 14 C4 4 48 4 48 14 L48 18 L38 18 L36 12 L16 12 L14 18 L4 18 Z"/>
    <path fill="var(--orange)" d="M14 20 L38 20 L46 40 L6 40 Z"/>
    <circle cx="26" cy="29" r="6" fill="var(--paper)"/>
    <circle cx="26" cy="29" r="3" fill="var(--orange)"/>
  </svg>
  <p class="phone-number">9000 4127</p>
  <p class="web-address">brightwellcare.com.au</p>
</main>
</body>
</html>
```